Gentleman's grooming products require a business card

I need a business card that incorporates the logo [ or parts of ] that we had Pixel Hive design for us as uploaded.

We sell online, mens grooming products including moustache waxes, beard oils and shaving accessories.
We want a card that is classy, professional and a card that shouts mens products.

Target Market(s)

Young professional male market

Industry/Entity Type

Business

Contact Information for Business Card

Ross and Edith Carwell
Lather and Lore
Purveyors of gentleman's stiffeners and grooming requisites
M :0418529647
E : ross@latherandlore.com.au
E : edith@latherandlore.com.au
E : sales@theblokesbalmery.com.au

W : www.latherandlore.com.au

Requirements
Must have
• Class
Nice to have
• Professionalism

```html
<!DOCTYPE html>
<html lang="en">
<head>
<meta charset="utf-8">
<title>Lather and Lore – Business Card</title>
<link rel="stylesheet" href="https://fonts.googleapis.com/css2?family=Open+Sans:wght@400;600&display=swap">
<style>
  :root {
    --backdrop: #3a312c;
    --card: #141414;
    --card-edge: #1d1d1d;
    --ink: #f2f2f2;
    --gold: #e0b81c;
  }
  * { box-sizing: border-box; margin: 0; padding: 0; }
  html, body { width: 1200px; height: 780px; overflow: hidden; }
  body {
    background: var(--backdrop);
    font-family: "Open Sans", Arial, sans-serif;
    color: var(--ink);
  }
  .canvas {
    width: 1200px; height: 780px;
    display: flex; align-items: center; justify-content: center; gap: 60px;
  }
  .card {
    position: relative;
    width: 540px; height: 309px;
    background: var(--card);
    border: 1px solid var(--card-edge);
    border-radius: 4px;
    box-shadow: 0 18px 40px rgba(0,0,0,.45);
    overflow: hidden;
  }
  .brand-name {
    position: absolute;
    font-family: "Open Sans", Arial, sans-serif;
    font-weight: 400;
    font-size: 34px;
    letter-spacing: 1px;
    color: var(--ink);
    line-height: 1.1;
    text-align: center;
  }
  /* front */
  .card-front .brand-name { left: 0; right: 0; top: 118px; }
  .website {
    position: absolute; left: 0; right: 0; top: 196px;
    text-align: center;
    color: var(--gold);
    font-size: 15px; font-weight: 600;
  }
  /* back */
  .card-back .brand-name { left: 150px; right: 20px; top: 62px; }
  .rule { position: absolute; height: 2px; background: var(--gold); }
  .rule-left { left: 0; width: 150px; top: 150px; }
  .rule-right { right: 0; width: 130px; top: 252px; }
  .contact-name {
    position: absolute; left: 160px; top: 139px;
    font-size: 16px; letter-spacing: .5px;
    text-transform: uppercase;
    white-space: nowrap;
  }
  .contact-list {
    position: absolute; left: 110px; top: 178px;
    list-style: none;
    font-size: 15px; line-height: 21px;
    white-space: nowrap;
  }
  .contact-list .label { color: var(--gold); margin-right: 4px; }
</style>
</head>
<body>
  <main class="canvas">
    <section class="card card-front" aria-label="Card front">
      <div class="brand-name">Lather and Lore</div>
      <div class="website">www.latherandlore.com.au</div>
    </section>

    <section class="card card-back" aria-label="Card back">
      <div class="brand-name">Lather and Lore</div>
      <span class="rule rule-left"></span>
      <div class="contact-name">Ross and Edith Carwell</div>
      <ul class="contact-list">
        <li><span class="label">M:</span>0418529647</li>
        <li><span class="label">E:</span>ross@latherandlore.com.au</li>
        <li><span class="label">E:</span>edith@latherandlore.com.au</li>
        <li><span class="label">E:</span>sales@theblokesbalmery.com.au</li>
      </ul>
      <span class="rule rule-right"></span>
    </section>
  </main>
</body>
</html>
```